Business Card template designs

We need a lot of Business card designs.
Your designs will get exposure on our newly opened business-card printing website.
We are committed to quality of paper and packages we use, so they will come up very fancy.

Here is your advantage. We will put the profile of the graphic designer on our site so that you can showcase your designs to people around the world and in Japan.

A profile is not mandatory, although we encourage graphic designers to have a profile to get continuous work in the future.
We are looking forward to having many good designs.

The right of the use of design will be owned by us.
The design may be used to the products other than
business cards.

Target Market(s)

designer,photographer,creator,artist

Industry/Entity Type

Printing

Contact Information for Business Card

The back design is important.
Please check the reference file.

Requirements
Must have
• Please include the following, required information on your business card designs.
• Name: Haruna Okabe
• Title: Designer
• Web: https://www.ketori.co.jp/kt/
• Address: 4-17 Kamiharuta-Cho Meguro-ku, Tokyo
• Email: info@kketori.com
• Phone: 03 4816 3907
• Mobile: 070 2143 6658
• * For Japanese sites, we will convert the text portion to Japanese characters.
• * In case of 28mmx70mm only include Name,Enail,Phone and SNS account(https://www.facebook.com/kketori.com)
• 1. colorful
• 2. simple
• 3. natural
• 4. modern
• 5. cool
• 6. sporty
• Please make variations of the same image with 3-6
• different colors / patterns for one design so that
• customers can compare and choose.
• If you want to use a same picture, please make make
• copies and paste on each different types of design.
Nice to have
• You may also use, the following non-required information.
• Company Name: Ketori, Inc.
• Fax: 03-4173-9620
• Open space for company logo

```html
<!DOCTYPE html>
<html lang="en">
<head>
<meta charset="utf-8">
<title>Ketori Business Card – Haruna Okabe</title>
<link rel="stylesheet" href="https://fonts.googleapis.com/css2?family=Bebas+Neue&family=Roboto:wght@400;500;700&display=swap">
<style>
  :root {
    --backdrop: #d8d9db;
    --navy: #223f87;
    --sky: #3b9ad5;
    --orange: #f7941d;
    --white: #ffffff;
  }
  * { margin: 0; padding: 0; box-sizing: border-box; }
  html, body {
    width: 1200px;
    height: 1199px;
    overflow: hidden;
    background: var(--backdrop);
    font-family: "Roboto", Arial, sans-serif;
  }
  .sheet { position: relative; width: 1200px; height: 1199px; }

  .card {
    position: absolute;
    top: 225px;
    width: 427px;
    height: 748px;
  }
  .card--front { left: 129px; background: var(--navy); }
  .card--back  { left: 640px; background: var(--sky); }

  /* Front side */
  .profile {
    position: absolute;
    right: 39px;
    top: 450px;
    width: 250px;
    text-align: right;
  }
  .profile__name {
    font-family: "Bebas Neue", "Arial Narrow", sans-serif;
    font-weight: 400;
    font-size: 38px;
    line-height: 1;
    letter-spacing: 0.5px;
    color: var(--orange);
  }
  .profile__title {
    color: var(--white);
    font-size: 17px;
    line-height: 1;
    margin-top: 2px;
  }
  .profile__rule {
    width: 184px;
    height: 8px;
    background: var(--orange);
    margin: 14px 0 0 auto;
  }
  .contact-list {
    list-style: none;
    margin-top: 22px;
  }
  .contact-list__item {
    display: flex;
    justify-content: flex-end;
    align-items: center;
    gap: 10px;
    color: var(--white);
    font-size: 16px;
    line-height: 28.5px;
  }
  .contact-list__icon { width: 14px; height: 14px; flex: none; }
  .address {
    margin-top: 9px;
    margin-right: 24px;
    color: var(--white);
    font-size: 16px;
    line-height: 22px;
    font-style: normal;
  }

  /* Back side */
  .brand {
    position: absolute;
    left: 50px;
    top: 300px;
    font-family: "Roboto", Arial, sans-serif;
    font-weight: 500;
    font-size: 92px;
    line-height: 1;
    color: var(--navy);
    letter-spacing: 1px;
  }
  .fax {
    position: absolute;
    right: 48px;
    top: 423px;
    display: flex;
    align-items: center;
    gap: 6px;
    color: var(--navy);
    font-weight: 700;
    font-size: 16px;
  }
  .fax__icon { width: 15px; height: 14px; }
  .back-rule {
    position: absolute;
    left: 50px;
    right: 47px;
    top: 472px;
    height: 9px;
    background: var(--orange);
  }
</style>
</head>
<body>
<main class="sheet">

  <section class="card card--front" aria-label="Business card front">
    <div class="profile">
      <h1 class="profile__name">HARUNA OKABE</h1>
      <p class="profile__title">Designer</p>
      <div class="profile__rule"></div>

      <ul class="contact-list">
        <li class="contact-list__item">
          <span>03 4816 3907</span>
          <svg class="contact-list__icon" viewBox="0 0 14 14" aria-hidden="true">
            <path d="M3 1.5l2 2.8-1.2 1.3c.8 1.8 2 3 3.8 3.9L9 8.2l3 1.8-.8 2.3c-5.2-.4-9-4.4-9.4-9.6z" fill="none" stroke="#f7941d" stroke-width="1.4" stroke-linejoin="round"/>
          </svg>
        </li>
        <li class="contact-list__item">
          <span>070 2143 6658</span>
          <svg class="contact-list__icon" viewBox="0 0 14 14" aria-hidden="true">
            <rect x="3.5" y="1" width="7" height="12" rx="1.2" fill="none" stroke="#f7941d" stroke-width="1.4"/>
            <rect x="6" y="10.3" width="2" height="1.2" fill="#f7941d"/>
          </svg>
        </li>
        <li class="contact-list__item">
          <span>info@kketori.com</span>
          <svg class="contact-list__icon" viewBox="0 0 14 14" aria-hidden="true">
            <rect x="1" y="3" width="12" height="8.5" rx="1" fill="none" stroke="#f7941d" stroke-width="1.4"/>
            <path d="M1.5 3.8L7 8l5.5-4.2" fill="none" stroke="#f7941d" stroke-width="1.4"/>
          </svg>
        </li>
        <li class="contact-list__item">
          <span>www.ketori.co.jp/kt/</span>
          <svg class="contact-list__icon" viewBox="0 0 14 14" aria-hidden="true">
            <circle cx="7" cy="7" r="5.8" fill="none" stroke="#f7941d" stroke-width="1.3"/>
            <ellipse cx="7" cy="7" rx="2.5" ry="5.8" fill="none" stroke="#f7941d" stroke-width="1.1"/>
            <path d="M1.2 7h11.6M2 4.2h10M2 9.8h10" stroke="#f7941d" stroke-width="1.1"/>
          </svg>
        </li>
      </ul>

      <address class="address">4-17 Kamiharuta-Cho<br>Meguro-ku, Tokyo</address>
    </div>
  </section>

  <section class="card card--back" aria-label="Business card back">
    <p class="brand">Ketori</p>
    <p class="fax">
      <svg class="fax__icon" viewBox="0 0 15 14" aria-hidden="true">
        <rect x="4" y="1" width="7" height="4" fill="#ffffff"/>
        <rect x="1" y="5" width="13" height="6" rx="1.5" fill="#ffffff"/>
        <rect x="4" y="9" width="7" height="4" fill="#ffffff" stroke="#3b9ad5" stroke-width="1"/>
      </svg>
      <span>03-4173-9620</span>
    </p>
    <div class="back-rule"></div>
  </section>

</main>
</body>
</html>
```